Business Card for New Greek Restaurant

Looking for a Business card for a new Greek Restaurant that's focus is on Take out and Delivery & catering.

Also to outline the contact information for the restaurant.
Does not require a name or title of a specific person (Just general business card)
Phone (519) 731-FOOD (3663)
Email : info@bluefigkitchen.ca
Website : www.bluefigkitchen.ca

Facebook/Instagram/Twitter Icons to Follow us as well.

TAKEOUT * DELIVERY* CATERING

Target Market(s)

Woman Age 25-44

Industry/Entity Type

Greek Restaurant

Contact Information for Business Card

Card is to have the general contact information for the business as well as outline our Take Out and Catering Services. Existing Logo attached and to be incorporated into the design.

Font styles to use
Sans Serif

Colors

Designer to choose colors to be used in the design.

Requirements
Must have
• Restaurant Contact Information :
• Phone (519) 731-FOOD (3663)
• Email : info@bluefigkitchen.ca
• Website : www.bluefigkitchen.ca
• Highlight Takeout, Catering, Delivery
• Business Address :
• Maplerow Plaza
• 47 Carden Ave., Unit 6
• Breslau ON
• N0K 2P5
Nice to have
• Modern Feel to promote TakeOut and Catering Services.
Should not have
• No Specific Title or Contact Person (Generic Business Card for Restaurant)

```html
<!DOCTYPE html>
<html lang="en">
<head>
<meta charset="utf-8">
<title>Blue Fig Kitchen – Business Card</title>
<link rel="stylesheet" href="https://fonts.googleapis.com/css2?family=Work+Sans:wght@400;500;600&family=Roboto+Condensed:wght@500&display=swap">
<style>
  :root {
    --backdrop: #d8c8b0;
    --card-frost: #ece7df;
    --band: #4b4743;
    --band-texture-light: #8a8580;
    --teal: #2a9fb0;
    --text-light: #d9d4cc;
    --text-muted: #b9b3aa;
  }
  html, body {
    margin: 0;
    width: 1200px;
    height: 1047px;
    overflow: hidden;
    background: var(--backdrop);
  }
  .card {
    position: absolute;
    left: 100px;
    top: 48px;
    width: 1000px;
    height: 950px;
    border-radius: 44px;
    overflow: hidden;
    background: var(--card-frost);
    font-family: "Work Sans", sans-serif;
  }
  .brand {
    position: absolute;
    top: 0;
    left: 0;
    width: 100%;
    height: 476px;
    display: flex;
    flex-direction: column;
    align-items: center;
    justify-content: center;
    gap: 18px;
  }
  .brand-name {
    font-size: 76px;
    font-weight: 600;
    color: var(--teal);
    letter-spacing: 2px;
    text-transform: uppercase;
    margin: 0;
  }
  .brand-tagline {
    font-size: 30px;
    font-weight: 400;
    color: var(--teal);
    letter-spacing: 8px;
    text-transform: uppercase;
    margin: 0;
  }
  .info-band {
    position: absolute;
    left: 0;
    top: 476px;
    width: 100%;
    height: 474px;
    background: var(--band);
  }
  .band-texture {
    position: absolute;
    left: 170px;
    top: 0;
    width: 150px;
    height: 100%;
    background: linear-gradient(90deg, transparent, var(--band-texture-light) 40%, var(--band-texture-light) 60%, transparent);
    opacity: 0.45;
  }
  .follow {
    position: absolute;
    top: 76px;
    left: 0;
    width: 100%;
    display: flex;
    justify-content: center;
    align-items: center;
    gap: 14px;
    font-size: 34px;
    color: var(--text-light);
  }
  .follow-label { margin-right: 10px; }
  .social-dot {
    width: 40px;
    height: 40px;
    border-radius: 50%;
    background: var(--teal);
  }
  .contact {
    position: absolute;
    top: 210px;
    left: 264px;
    margin: 0;
    font-size: 31px;
    line-height: 42px;
    color: var(--text-light);
    list-style: none;
    padding: 0;
  }
  .contact-key { color: var(--teal); margin-right: 12px; }
  .services {
    position: absolute;
    top: 366px;
    left: 0;
    width: 100%;
    height: 60px;
  }
  .services-rule {
    position: absolute;
    top: 29px;
    height: 4px;
    background: var(--teal);
  }
  .services-rule.left { left: 0; width: 190px; }
  .services-rule.right { right: 0; width: 190px; }
  .services-text {
    position: absolute;
    top: 0;
    left: 0;
    width: 100%;
    text-align: center;
    font-family: "Roboto Condensed", sans-serif;
    font-weight: 500;
    font-size: 36px;
    line-height: 60px;
    color: var(--text-muted);
    margin: 0;
  }
</style>
</head>
<body>
  <main class="card">
    <header class="brand">
      <h1 class="brand-name">Blue Fig Kitchen</h1>
      <p class="brand-tagline">Fresh Grill</p>
    </header>

    <section class="info-band">
      <div class="band-texture" role="img" aria-label="Speckled stone texture strip"></div>

      <div class="follow">
        <span class="follow-label">Follow us</span>
        <span class="social-dot" aria-label="Social profile"></span>
        <span class="social-dot" aria-label="Social profile"></span>
        <span class="social-dot" aria-label="Social profile"></span>
      </div>

      <ul class="contact">
        <li><span class="contact-key">P :</span>(519) 731-FOOD (3663)</li>
        <li><span class="contact-key">E :</span>info@bluefigkitchen.ca</li>
        <li><span class="contact-key">W :</span>www.bluefigkitchen.ca</li>
      </ul>

      <div class="services">
        <span class="services-rule left"></span>
        <p class="services-text">TAKEOUT * DELIVERY* CATERING</p>
        <span class="services-rule right"></span>
      </div>
    </section>
  </main>
</body>
</html>
```